QUILTa Inc. eCommerce
QUILTa Inc. (Science, Technology, Engineering, Arts & Math development)
QUILTa Inc.  eCommerce  - Technology Transfer
Creative Brief
Bright & Fun-filled
Dalia P. Corwen
CEO and Founder
4730 Marrowby Ln Ashburn, VA 20163
dalia.corwen@quiltainc.org
This is a non-profit organization providing technology mentoring and education to girls. The business card should be professional but convey technology and cutting edge with appeal to the young and also business grantors
To inspire, empower, mentor and develop girls Bright Path onward
dpcorwen dpcorwen
For the QUILTa eCommerence business card and stationary project, I would like a few changes: Front of card change to "Founder and CEO" (not CEO and Founder) Add "Inc" next to the "d" in QUILTa under QUILTa add "Science, Technology, Engineering, Arts & Math Development" (this is what QUILTa stands for) Back of card "QUILTa" "To inspire, empower, mentor & develop girls" "Bright Path onward"

```html
<!DOCTYPE html>
<html lang="en">
<head>
<meta charset="utf-8">
<title>QUILTa Inc. Stationery Set</title>
<link rel="stylesheet" href="https://fonts.googleapis.com/css2?family=Marcellus&family=Open+Sans:wght@400;600&display=swap">
<style>
  :root {
    --purple: #8c2a8e;
    --purple-deep: #6f1f74;
    --purple-light: #a83aa8;
    --orange: #f08a2c;
    --paper: #ffffff;
    --ink: #555;
    --stage: #ececee;
    --brand-font: "Marcellus", serif;
    --text-font: "Open Sans", sans-serif;
  }
  * { box-sizing: border-box; margin: 0; padding: 0; }
  html, body { width: 1200px; height: 937px; overflow: hidden; }
  body { background: var(--stage); font-family: var(--text-font); color: var(--ink); position: relative; }

  .sheet { position: absolute; background: var(--paper); box-shadow: 0 2px 6px rgba(0,0,0,.18); overflow: hidden; }
  .sheet svg.swoosh { position: absolute; inset: 0; width: 100%; height: 100%; }

  .brand { position: absolute; font-family: var(--brand-font); font-weight: 400; color: var(--purple); line-height: 1; letter-spacing: .04em; white-space: nowrap; }

  /* Letterhead */
  .letterhead { left: 66px; top: 46px; width: 506px; height: 566px; }
  .letterhead .brand { left: 36px; top: 58px; font-size: 32px; }
  .letter-body { position: absolute; left: 36px; top: 128px; width: 420px; font-size: 6.3px; line-height: 1.55; }
  .letter-body p { margin-bottom: 9px; }
  .letter-sign { font-family: var(--brand-font); font-size: 13px; color: #333; margin: 4px 0; }
  .letter-contact { position: absolute; left: 408px; top: 470px; font-size: 6px; line-height: 1.7; color: #fff; font-style: normal; }

  /* Folder */
  .folder { left: 635px; top: 35px; width: 461px; height: 583px; }
  .folder .brand { left: 96px; top: 258px; font-size: 66px; }

  /* Business cards */
  .card-front { left: 46px; top: 653px; width: 177px; height: 106px; }
  .card-front .brand { left: 9px; top: 14px; font-size: 15px; }
  .card-descriptor { position: absolute; left: 9px; top: 33px; width: 80px; font-size: 3.9px; line-height: 1.4; color: var(--ink); }
  .card-details { position: absolute; right: 9px; top: 12px; font-size: 4.6px; line-height: 1.6; text-align: right; color: var(--ink); }
  .card-details .card-name { font-weight: 600; color: var(--purple); font-size: 5.4px; }
  .card-back { left: 46px; top: 785px; width: 177px; height: 101px; }
  .card-back-content { position: absolute; inset: 0; display: flex; flex-direction: column; align-items: center; justify-content: center; text-align: center; gap: 4px; }
  .card-back-content .brand { position: static; font-size: 15px; }
  .card-mission { font-size: 5px; color: var(--ink); }
  .card-tagline { font-size: 5.4px; font-weight: 600; color: var(--orange); }

  /* Envelopes */
  .envelope-front { left: 263px; top: 671px; width: 433px; height: 202px; }
  .envelope-front .brand { left: 40px; top: 62px; font-size: 38px; }
  .envelope-back { left: 737px; top: 671px; width: 415px; height: 202px; }
  .envelope-web { position: absolute; left: 0; right: 0; top: 22px; text-align: center; color: #fff; font-size: 8.5px; letter-spacing: .35em; }
</style>
</head>
<body>

<section class="sheet letterhead" aria-label="Letterhead">
  <svg class="swoosh" viewBox="0 0 506 566" preserveAspectRatio="none">
    <defs>
      <linearGradient id="lh-fill" x1="0" y1="1" x2="1" y2="0">
        <stop offset="0" stop-color="#6f1f74"/>
        <stop offset="1" stop-color="#a83aa8"/>
      </linearGradient>
    </defs>
    <path d="M150 566 Q 410 525 506 360 L 506 566 Z" fill="#f08a2c"/>
    <path d="M172 566 Q 420 530 506 372 L 506 566 Z" fill="url(#lh-fill)"/>
  </svg>
  <div class="brand">QUILTa</div>
  <div class="letter-body">
    <p>July 3, 2024<br>Dear Reader,</p>
    <p>Thank you for your interest in our mentoring programs. Our team brings girls together with engineers, artists and scientists who share their work and guide each new project from idea to launch.</p>
    <p>We would welcome the chance to meet and discuss how your support can open more classroom seats this year.</p>
    <p>Each season our students build apps, robots and art pieces that they present to families and partners at an open showcase. Your help makes these evenings possible for every girl who joins.</p>
    <p>Kind regards,</p>
    <div class="letter-sign">Dalia</div>
    <p>Dalia P. Corwen<br>Founder and CEO<br>4730 Marrowby Ln Ashburn, VA 20163</p>
  </div>
  <address class="letter-contact">
    4730 Marrowby Ln<br>Ashburn, VA 20163<br>(703) 555-0148<br>dalia.corwen@quiltainc.org<br>www.quiltainc.org
  </address>
</section>

<section class="sheet folder" aria-label="Presentation folder">
  <svg class="swoosh" viewBox="0 0 461 583" preserveAspectRatio="none">
    <defs>
      <linearGradient id="fd-fill" x1="0" y1="0" x2="1" y2="1">
        <stop offset="0" stop-color="#a83aa8"/>
        <stop offset="1" stop-color="#6f1f74"/>
      </linearGradient>
    </defs>
    <path d="M44 0 C 320 110 440 320 452 583 L 461 583 L 461 0 Z" fill="#f08a2c"/>
    <path d="M62 0 C 334 112 452 322 461 560 L 461 0 Z" fill="url(#fd-fill)"/>
  </svg>
  <div class="brand">QUILTa</div>
</section>

<section class="sheet card-front" aria-label="Business card front">
  <svg class="swoosh" viewBox="0 0 177 106" preserveAspectRatio="none">
    <path d="M60 106 Q 140 92 177 46 L 177 106 Z" fill="#f08a2c"/>
    <path d="M70 106 Q 146 94 177 52 L 177 106 Z" fill="#8c2a8e"/>
  </svg>
  <div class="brand">QUILTa Inc</div>
  <div class="card-descriptor">Science, Technology, Engineering, Arts &amp; Math Development</div>
  <div class="card-details">
    <div class="card-name">Dalia P. Corwen</div>
    <div>Founder and CEO</div>
    <div>(703) 555-0148</div>
    <div>dalia.corwen@quiltainc.org</div>
  </div>
</section>

<section class="sheet card-back" aria-label="Business card back">
  <div class="card-back-content">
    <div class="brand">QUILTa</div>
    <div class="card-mission">To inspire, empower, mentor &amp; develop girls</div>
    <div class="card-tagline">Bright Path onward</div>
  </div>
</section>

<section class="sheet envelope-front" aria-label="Envelope front">
  <svg class="swoosh" viewBox="0 0 433 202" preserveAspectRatio="none">
    <defs>
      <linearGradient id="ev-fill" x1="0" y1="0" x2="1" y2="1">
        <stop offset="0" stop-color="#a83aa8"/>
        <stop offset="1" stop-color="#6f1f74"/>
      </linearGradient>
    </defs>
    <path d="M80 0 Q 330 50 433 196 L 433 0 Z" fill="#f08a2c"/>
    <path d="M94 0 Q 338 50 433 184 L 433 0 Z" fill="url(#ev-fill)"/>
  </svg>
  <div class="brand">QUILTa</div>
</section>

<section class="sheet envelope-back" aria-label="Envelope back">
  <svg class="swoosh" viewBox="0 0 415 202" preserveAspectRatio="none">
    <path d="M0 0 H415 V62 L207 98 L0 62 Z" fill="#f08a2c"/>
    <path d="M0 0 H415 V56 L207 92 L0 56 Z" fill="#8c2a8e"/>
  </svg>
  <div class="envelope-web">www.quiltainc.org</div>
</section>

</body>
</html>
```